Rent a Velvet needs a Stunning web design

Rent a Velvet is an upmarket agency in Sydney that has lingerie waitresses for events.

Rent a Velvet is looking for a website design that is as sexy and sophisticated as the ladies who work for them!

The design mustn't be cluttered, tacky or pornographic. What I'm looking for is something better than the industry leader www.glimmerdolls.com.au Something classy, sexy and different.

When designing please suggest a CMS, we already use wordpress but are open to suggestions.

We will need a home page that incorporates a feed from a blog and/or social media (please make suggestions and use your discretion as a designer, however we'd like to approve what goes into the feed before it goes in.) The home page could also have a list of our services, but if not we will need a services page. Our Services include:
Lingerie waitressing at events
Lingerie waitresses to help dress the groom pre wedding.
Bucks parties

We have a logo that we'd like incorporated into the design and have attached it.

We will also need a portfolio page for the ladies, This is not to be cluttered, tacky or pornographic. It needs to be classy.

We will also need a "Contact us" page and were thinking that this could potentially also be a "Ask for a quote on your event" page. I.e. have a regular "Contact us" form but have alternate fields if they tick the "I want a quote" box. Alternatively you could have two parts to the contact us page. One that is a regular form and one that has a "Your requirements" box.

Again please use your discretion when designing these, if it's too cluttered it won't work. If it looks tacky, don't do it. If you have suggestions make them.

Target Market(s)

Males between the ages of 18 - 45

Industry/Entity Type

Industry

Requirements
Must have
• Must incorporate our logo.

```html
<!DOCTYPE html>
<html lang="en">
<head>
<meta charset="utf-8">
<title>Rent a Velvet – Our Ladies</title>
<link href="https://fonts.googleapis.com/css2?family=Gelasio:ital,wght@0,400;0,600;0,700;1,400&family=Source+Sans+3:ital,wght@0,400;0,600;1,400&display=swap" rel="stylesheet">
<style>
:root{
  --black:#000;
  --strip:#3c3c3c;
  --red:#e3173e;
  --blue-top:#1d93dc;
  --blue-bottom:#0b5ca6;
  --nav-line:#4aa6df;
  --text:#555;
  --heading-text:#333;
  --rule:#d8d8d8;
  --footer:#343434;
  --footer-text:#e8e8e8;
  --white:#fff;
  --search:#2b2b2b;
}
*{box-sizing:border-box;margin:0;padding:0}
html,body{width:1061px;height:1200px;overflow:hidden;background:var(--white)}
body{font-family:"Source Sans 3",Arial,sans-serif;color:var(--text);position:relative}
.top-strip{height:5px;background:var(--strip)}
.site-header{height:122px;background:var(--black);position:relative}
.brand{position:absolute;left:37px;top:40px;display:flex;align-items:center;gap:12px}
.brand-name{font-family:"Gelasio",Georgia,serif;font-weight:700;font-size:36px;color:var(--red);white-space:nowrap}
.brand-dot{width:14px;height:14px;border-radius:50%;background:var(--red)}
.booking{position:absolute;right:172px;top:22px;font-family:"Gelasio",Georgia,serif;color:#bbb;font-size:17px;white-space:nowrap}
.booking strong{color:var(--white);font-weight:400;font-size:21px;margin-left:4px}
.social{position:absolute;right:25px;top:18px;display:flex;gap:4px}
.social span{width:29px;height:29px;border-radius:50%;background:var(--white);display:block}
.search{position:absolute;right:25px;top:70px;width:248px;height:31px;border-radius:16px;background:var(--search);color:#ccc;font-size:12px;padding:7px 18px;display:flex;justify-content:space-between;align-items:center}
.main-nav{height:53px;background:linear-gradient(var(--blue-top),var(--blue-bottom));display:flex}
.main-nav a{display:flex;align-items:center;justify-content:center;color:var(--white);text-decoration:none;font-family:"Gelasio",Georgia,serif;font-weight:600;font-size:14.5px;border-right:1px solid var(--nav-line);white-space:nowrap}
.main-nav a:last-child{border-right:none}
.content{padding:0 34px 0 27px}
.page-title{font-family:"Gelasio",Georgia,serif;font-weight:600;color:var(--red);font-size:23px;margin-top:40px;padding-bottom:6px;border-bottom:1px solid var(--rule)}
.lead{font-style:italic;font-size:15px;color:var(--heading-text);margin:13px 0 7px}
.content p.body{font-size:13px;line-height:20.5px;margin-bottom:5px}
.gallery{display:grid;grid-template-columns:repeat(3,206px);gap:12px 9px;margin-top:30px}
.photo{height:155px;border:1px solid #e2e2e2}
.p1{background:linear-gradient(135deg,#f3ece8,#a8452c 55%,#e9d2c2)}
.p2{background:linear-gradient(160deg,#f5f5f5,#b98a74 45%,#3d9bd6)}
.p3{background:linear-gradient(160deg,#eeeae6,#b08b74 50%,#f0e9e3)}
.p4{background:linear-gradient(160deg,#f0f0f0,#d4ab98 50%,#b04aa4)}
.p5{background:linear-gradient(160deg,#dfe4ea,#c19a7c 50%,#e6dfd6)}
.p6{background:linear-gradient(160deg,#d4d4d4,#b58a6e 50%,#6b5b58)}
.tagline{font-style:italic;font-size:12.5px;line-height:20.5px;color:#444;margin-top:40px}
.share-row{display:flex;gap:12px;margin-top:12px}
.share{display:flex;align-items:center;gap:5px}
.share b{height:20px;padding:0 9px;border-radius:3px;color:var(--white);font-size:11px;font-weight:600;display:flex;align-items:center}
.share i{font-style:normal;font-size:11px;border:1px solid #ccc;border-radius:3px;height:20px;padding:0 5px;display:flex;align-items:center;color:#333}
.s-tw b{background:#2d9ad8}.s-fb b{background:#5b74a8}.s-gn b{background:#2f8a34}
.site-footer{position:absolute;left:0;right:0;top:1048px;bottom:0;background:var(--footer);color:var(--footer-text)}
.footer-social{position:absolute;left:29px;top:17px;display:flex;gap:3px}
.footer-social span{width:26px;height:26px;border-radius:50%;background:var(--white);display:block}
.footer-nav{position:absolute;left:31px;top:62px;display:flex;gap:26px;font-size:12px}
.footer-nav a{color:var(--footer-text);text-decoration:none}
.copyright{position:absolute;left:26px;top:90px;font-size:10.5px}
.footer-brand{position:absolute;right:48px;top:36px;font-family:"Gelasio",Georgia,serif;font-weight:700;font-size:29px;color:#bdbdbd;white-space:nowrap}
</style>
</head>
<body>
<div class="top-strip"></div>
<header class="site-header">
  <div class="brand"><span class="brand-name">Rent a Velvet</span><span class="brand-dot"></span></div>
  <div class="booking">For Booking: <strong>555 014 2288</strong></div>
  <div class="social"><span></span><span></span><span></span><span></span></div>
  <div class="search">Search here..
    <svg width="14" height="14" viewBox="0 0 14 14"><circle cx="6" cy="6" r="4.5" fill="none" stroke="#ccc" stroke-width="2"/><line x1="9.5" y1="9.5" x2="13" y2="13" stroke="#ccc" stroke-width="2"/></svg>
  </div>
</header>
<nav class="main-nav">
  <a href="#" style="width:120px">HOME</a>
  <a href="#" style="width:125px">ABOUT US</a>
  <a href="#" style="width:133px">OUR LADIES</a>
  <a href="#" style="width:145px">WAITRESSES</a>
  <a href="#" style="width:112px">VENUES</a>
  <a href="#" style="width:108px">EVENTS</a>
  <a href="#" style="width:124px">BOOKING</a>
  <a href="#" style="width:134px">CONTACT US</a>
</nav>
<main class="content">
  <h1 class="page-title">Our Ladies</h1>
  <p class="lead">Lorem ipsum dolor sit amet, consectetuer adipiscing elit. Nam cursus.</p>
  <p class="body">Morbi ut mi. Nullam enim leo, egestas id, condimentum at, laoreet mattis, massa. Sed eleifend nonummy diam. Praesent mauris ante, elementum et, bibendum at, posuere sit amet, nibh. Duis tincidunt lectus quis dui viverra vestibulum.</p>
  <p class="body">Suspendisse vulputate aliquam dui. Nulla elementum dui ut augue.</p>
  <p class="body">In iaculis facilisis massa. Etiam eu urna. Sed porta. Suspendisse quam leo, molestie sed, luctus quis, feugiat in, pede. Fusce tellus. Sed metus augue, convallis et, vehicula ut, pulvinar eu, ante. Integer orci tellus, tristique vitae, consequat nec, porta vel, lectus. Nulla sit amet diam. Duis non nunc. Nulla rhoncus dictum metus. Curabitur tristique mi condimentum orci. Phasellus pellentesque aliquam enim. Proin dui lectus, cursus eu, mattis laoreet, viverra sit amet, quam. Curabitur vel dolor ultrices ipsum dictum tristique. Praesent vitae lacus. Ut velit enim, vestibulum non, fermentum nec, hendrerit quis, leo. Pellentesque rutrum malesuada neque.</p>
  <div class="gallery">
    <div class="photo p1" role="img" aria-label="Portrait photo of a red-haired hostess"></div>
    <div class="photo p2" role="img" aria-label="Portrait photo of a hostess in blue"></div>
    <div class="photo p3" role="img" aria-label="Portrait photo of a hostess in white"></div>
    <div class="photo p4" role="img" aria-label="Portrait photo of a short-haired hostess"></div>
    <div class="photo p5" role="img" aria-label="Portrait photo of a blonde hostess"></div>
    <div class="photo p6" role="img" aria-label="Portrait photo of a brunette hostess"></div>
  </div>
  <p class="tagline">You've seen them on the runway and on the cover of various Australian lifestyle magazines. Now, you can book the Velvet ladies to wait at your private event. Whether you are having a bucks night, birthday party, harbour cruise or a wedding morning, the Velvet ladies can be there! Simply browse their portfolio here and then request your favourite hostess!</p>
  <div class="share-row">
    <div class="share s-tw"><b>Tweet</b><i>8</i></div>
    <div class="share s-fb"><b>Share</b><i>31</i></div>
    <div class="share s-gn"><b>Share</b><i>54</i></div>
  </div>
</main>
<footer class="site-footer">
  <div class="footer-social"><span></span><span></span><span></span><span></span></div>
  <nav class="footer-nav">
    <a href="#">Home</a><a href="#">About Us</a><a href="#">Our Ladies</a><a href="#">Waitresses</a><a href="#">Venues</a><a href="#">Events</a><a href="#">Booking</a><a href="#">Contact Us</a>
  </nav>
  <p class="copyright">© 2012 Company Name. All right reserved. Term of Use</p>
  <div class="footer-brand">Rent a Velvet</div>
</footer>
</body>
</html>
```